Business Card Design for Engineering Firm

Need a business card design for small mechanical and plumbing engineering form based in Utah. Design should be customizable for all employees.

```html
<!DOCTYPE html>
<html lang="en">
<head>
<meta charset="utf-8">
<title>Wasatch Ridge Engineering – Business Card</title>
<link rel="stylesheet" href="https://fonts.googleapis.com/css2?family=Montserrat:wght@500;600;700&display=swap">
<style>
  :root {
    --bg: #2b2b2b;
    --card: #ffffff;
    --brand-red: #8b1418;
    --ink-grey: #555759;
    --text-dark: #2a2a2a;
    --shadow: rgba(0, 0, 0, 0.45);
  }
  * { box-sizing: border-box; margin: 0; padding: 0; }
  html, body {
    width: 1200px;
    height: 880px;
    overflow: hidden;
    background: var(--bg);
    font-family: "Montserrat", Arial, sans-serif;
  }
  .stage {
    position: relative;
    width: 1200px;
    height: 880px;
  }
  .card {
    position: absolute;
    width: 600px;
    height: 343px;
    background: var(--card);
    box-shadow: 0 14px 30px var(--shadow);
    overflow: hidden;
  }
  .card--front { left: 150px; top: 70px; }
  .card--back  { left: 450px; top: 467px; }

  /* brand wordmark */
  .wordmark {
    display: flex;
    align-items: center;
    gap: 14px;
    color: var(--brand-red);
    font-weight: 700;
    text-transform: uppercase;
    line-height: 1.1;
  }
  .wordmark__square {
    width: 22px;
    height: 22px;
    background: var(--brand-red);
    flex-shrink: 0;
  }
  .card--front .wordmark {
    position: absolute;
    left: 50%;
    top: 50%;
    transform: translate(-50%, -50%);
    font-size: 34px;
    letter-spacing: 1px;
  }
  .card--back .wordmark {
    position: absolute;
    left: 40px;
    top: 50%;
    transform: translateY(-50%);
    font-size: 24px;
    letter-spacing: 0.5px;
    gap: 10px;
  }
  .card--back .wordmark__square { width: 16px; height: 16px; }

  /* contact block */
  .divider {
    position: absolute;
    left: 302px;
    top: 74px;
    width: 2px;
    height: 196px;
    background: var(--brand-red);
  }
  .contact {
    position: absolute;
    left: 326px;
    top: 66px;
    color: var(--text-dark);
  }
  .contact__name {
    font-size: 21px;
    font-weight: 700;
    letter-spacing: 0.5px;
    text-transform: uppercase;
    color: var(--ink-grey);
  }
  .contact__surname { color: var(--brand-red); }
  .contact__title {
    font-size: 13px;
    font-weight: 500;
    margin-top: 2px;
  }
  .contact__address {
    font-size: 13px;
    font-weight: 500;
    line-height: 1.4;
    margin-top: 12px;
  }
  .contact__list {
    list-style: none;
    margin-top: 12px;
    font-size: 13px;
    font-weight: 500;
  }
  .contact__item {
    display: flex;
    align-items: center;
    gap: 10px;
    margin-bottom: 7px;
  }
  .contact__icon {
    width: 14px;
    height: 14px;
    fill: var(--brand-red);
    flex-shrink: 0;
  }
</style>
</head>
<body>
<main class="stage">

  <section class="card card--front" aria-label="Card front">
    <div class="wordmark">
      <span class="wordmark__square"></span>
      <span>Wasatch Ridge<br>Engineering</span>
    </div>
  </section>

  <section class="card card--back" aria-label="Card back">
    <div class="wordmark">
      <span class="wordmark__square"></span>
      <span>Wasatch Ridge<br>Engineering</span>
    </div>

    <div class="divider"></div>

    <div class="contact">
      <p class="contact__name">Daniel <span class="contact__surname">Hartley</span></p>
      <p class="contact__title">Co-Founder</p>
      <p class="contact__address">P.O. Box 4412 Suite 3<br>Canyon Rd 18, Provo</p>
      <ul class="contact__list">
        <li class="contact__item">
          <svg class="contact__icon" viewBox="0 0 24 24" aria-hidden="true"><path d="M6.6 10.8a15.1 15.1 0 0 0 6.6 6.6l2.2-2.2a1 1 0 0 1 1-.25 11.4 11.4 0 0 0 3.6.57 1 1 0 0 1 1 1V20a1 1 0 0 1-1 1A17 17 0 0 1 3 4a1 1 0 0 1 1-1h3.5a1 1 0 0 1 1 1c0 1.25.2 2.45.57 3.6a1 1 0 0 1-.25 1z"/></svg>
          <span>801-555-0147</span>
        </li>
        <li class="contact__item">
          <svg class="contact__icon" viewBox="0 0 24 24" aria-hidden="true"><path d="M2 5h20v14H2z M3 6l9 7 9-7" /><path d="M2 5l10 8 10-8v2l-10 8L2 7z" fill="#fff"/></svg>
          <span>info@wasatchridge-eng.com</span>
        </li>
        <li class="contact__item">
          <svg class="contact__icon" viewBox="0 0 24 24" aria-hidden="true"><circle cx="12" cy="12" r="10"/><path d="M2 12h20M12 2c3 3 3 17 0 20M12 2c-3 3-3 17 0 20" stroke="#fff" stroke-width="1.4" fill="none"/></svg>
          <span>www.wasatchridge-eng.com</span>
        </li>
      </ul>
    </div>
  </section>

</main>
</body>
</html>
```